Civora - a Political Plebescite app.

There is a current app in the App Store (worldwide) and Play Store (worldwide) called voxPoll (with an owl logo). The UX needs to be redesigned to make it more visually pleasing.

The requirement is to build a UX that is suitable for both iOS and Android - i.e. consistent look for both platforms. The design is to span the variety of sizes available from smart devices - phones and tablets. The layout as it stands is portrait only, and a secondary design to encompass landscape is wanted.

You would need to download the app to get a feel for all the functionality - there are 3 visible forms (currently) and a hidden form, that will be used in the near future - this hidden form will look similar to the main (first) form.

To get full functionality you need to do the following:
Go to the Options page
Toggle the top slide
Click on UNREGISTERED
Select a state/territory

I know this is a bit non-intuitive - in the "real" product these steps are automated - but for this release the user gets to choose.

Once this is done - the other button(s) appear in the top left of the screen - and data is available to be displayed.

The current forms are included in this brief. The Options screen will ultimately not be showing all the current data, only the lower slider (or other indicator) and the associated version and copyright notices. The hidden screen is much like the main screen - showing the name of the bill and information pertaining to that bill - there needs to be a button (or action site) to toggle between the main and this hidden screen.

Target Market(s)

All eligable voters (currently in Australia)

Industry/Entity Type

Political

Requirements
Should not have
• Do not present to me my own/existing design with the only change being colours and label layout.

```html
<!DOCTYPE html>
<html lang="en">
<head>
<meta charset="utf-8">
<title>Civora – App Screens</title>
<link href="https://fonts.googleapis.com/css2?family=Roboto:wght@400;500&display=swap" rel="stylesheet">
<style>
  :root {
    --canvas: #cfcfcf;
    --screen: #ffffff;
    --bar: #000000;
    --bar-text: #ffffff;
    --panel: #f1f1f1;
    --line: #e2e2e2;
    --ink: #3c3c3c;
    --ink-soft: #555555;
    --label: #5a5a5a;
    --accent: #1e8ad6;
    --no: #ff2b1c;
    --party: #1f2d46;
    --yes: #1f9c3a;
    --toggle-on: #7fdca6;
    --toggle-off: #f4f4f4;
    --map-green: #3f8f5f;
    --map-red: #b8281c;
    --online: #19b43a;
    --link: #2a5db0;
  }
  * { box-sizing: border-box; margin: 0; padding: 0; }
  html, body { width: 1200px; height: 1000px; overflow: hidden; }
  body { background: var(--canvas); font-family: 'Roboto', Arial, sans-serif; position: relative; }

  .screen { position: absolute; top: 24px; width: 372px; height: 662px; background: var(--screen); overflow: hidden; }
  .screen--main { left: 24px; }
  .screen--options { left: 414px; }
  .screen--help { left: 804px; }

  .screen-caption { position: absolute; top: 716px; width: 372px; text-align: center; font-size: 34px; color: var(--label); }

  /* status bar */
  .status { position: absolute; top: 0; left: 0; right: 0; height: 24px; background: var(--bar); color: var(--bar-text); font-size: 14px; }
  .status__carrier { position: absolute; left: 8px; top: 4px; display: flex; align-items: center; gap: 5px; }
  .status__time { position: absolute; left: 0; right: 0; top: 4px; text-align: center; font-weight: 500; }
  .status__battery { position: absolute; right: 8px; top: 4px; display: flex; align-items: center; gap: 6px; }
  .battery { width: 26px; height: 11px; border: 1px solid #fff; padding: 1px; position: relative; }
  .battery::after { content: ""; position: absolute; right: -4px; top: 3px; width: 2px; height: 4px; background: #fff; }
  .battery span { display: block; width: 100%; height: 100%; background: #fff; }

  /* nav bar */
  .navbar { position: absolute; top: 24px; left: 0; right: 0; height: 48px; background: var(--bar); }
  .navbar__regions { position: absolute; left: 10px; top: 16px; display: flex; gap: 6px; }
  .region { width: 22px; height: 18px; border-radius: 4px; }
  .region--green { background: var(--map-green); }
  .region--red { background: var(--map-red); }
  .navbar__title { position: absolute; left: 0; right: 0; top: 15px; text-align: center; color: var(--bar-text); font-size: 16px; }
  .navbar__actions { position: absolute; right: 10px; top: 16px; display: flex; gap: 10px; }

  /* main screen */
  .bill-title { position: absolute; top: 72px; left: 0; right: 0; height: 34px; background: var(--panel); font-size: 15px; color: var(--ink); padding: 8px 10px; }
  .bill-title svg { position: absolute; right: 10px; top: 6px; }
  .bill-text { position: absolute; top: 116px; left: 10px; right: 10px; font-size: 10.4px; line-height: 15.6px; color: var(--ink-soft); hyphens: auto; -webkit-hyphens: auto; }
  .vote { position: absolute; top: 556px; left: 0; right: 0; display: flex; justify-content: center; gap: 16px; }
  .vote__item { width: 38px; text-align: center; font-size: 10px; }
  .vote__btn { width: 36px; height: 36px; border-radius: 50%; display: flex; align-items: center; justify-content: center; margin: 0 auto 6px; }
  .vote__item--no .vote__btn { background: var(--no); } .vote__item--no { color: var(--no); }
  .vote__item--party .vote__btn { background: var(--party); } .vote__item--party { color: var(--party); }
  .vote__item--yes .vote__btn { background: var(--yes); } .vote__item--yes { color: var(--yes); }

  /* footer bar */
  .footer { position: absolute; bottom: 0; left: 0; right: 0; height: 22px; background: var(--bar); color: #ddd; font-size: 10px; }
  .footer__dot { position: absolute; left: 10px; top: 7px; width: 8px; height: 8px; border-radius: 50%; background: var(--online); }
  .footer__chamber { position: absolute; left: 0; right: 0; top: 6px; text-align: center; }
  .footer__count { position: absolute; right: 10px; top: 6px; }

  /* options screen */
  .section-head { position: absolute; left: 0; right: 0; height: 37px; background: var(--panel); border-bottom: 1px solid var(--line); font-size: 15px; color: var(--ink); padding: 10px 10px; }
  .setting { position: absolute; left: 10px; right: 10px; height: 20px; font-size: 12.5px; color: var(--ink-soft); display: flex; justify-content: space-between; align-items: center; }
  .setting__value { color: var(--ink); }
  .toggle { width: 42px; height: 24px; border-radius: 12px; position: relative; border: 1px solid #e0e0e0; background: var(--toggle-off); }
  .toggle::after { content: ""; position: absolute; top: 1px; left: 1px; width: 20px; height: 20px; border-radius: 50%; background: #fff; box-shadow: 0 1px 3px rgba(0,0,0,.3); }
  .toggle--on { background: var(--toggle-on); border-color: var(--toggle-on); }
  .toggle--on::after { left: 19px; }
  .divider { position: absolute; left: 0; right: 0; height: 1px; background: var(--line); }
  .legal { position: absolute; top: 547px; left: 0; right: 0; height: 93px; background: #f7f7f7; padding: 14px 10px 0; font-size: 7.8px; line-height: 13px; color: #333; }
  .legal__version { font-weight: 500; }
  .legal a { color: var(--link); text-decoration: none; }

  /* help screen */
  .tabs { position: absolute; top: 72px; left: 0; right: 0; height: 34px; background: var(--panel); display: flex; }
  .tab { flex: 1; text-align: center; font-size: 13px; color: #555; padding-top: 10px; position: relative; }
  .tab + .tab::before { content: ""; position: absolute; left: 0; top: 6px; bottom: 6px; width: 1px; background: #d6d6d6; }
  .tab--active { color: var(--accent); background: #fff; border-bottom: 2px solid var(--accent); }
  .help-text { position: absolute; top: 116px; left: 10px; right: 10px; font-size: 10.4px; line-height: 15.6px; color: var(--ink-soft); hyphens: auto; -webkit-hyphens: auto; }
  .help-text p + p { margin-top: 15.6px; }
</style>
</head>
<body>

<!-- Main -->
<section class="screen screen--main">
  <div class="status">
    <div class="status__carrier">●●●○○ ORBIT
      <svg width="14" height="11" viewBox="0 0 14 11"><path d="M1 4a9 9 0 0 1 12 0M3.2 6.2a6 6 0 0 1 7.6 0M5.4 8.4a3 3 0 0 1 3.2 0" stroke="#fff" stroke-width="1.5" fill="none"/><circle cx="7" cy="10" r="1" fill="#fff"/></svg>
    </div>
    <div class="status__time">4:21 PM</div>
    <div class="status__battery">
      <svg width="8" height="12" viewBox="0 0 8 12"><path d="M1 3l6 5-3 3V1l3 3-6 5" stroke="#999" stroke-width="1.1" fill="none"/></svg>
      100% <div class="battery"><span></span></div>
    </div>
  </div>
  <div class="navbar">
    <div class="navbar__regions">
      <div class="region region--green" role="img" aria-label="Federal map button"></div>
      <div class="region region--red" role="img" aria-label="State map button, selected"></div>
      <div class="region region--green" role="img" aria-label="Federal map button"></div>
      <div class="region region--red" role="img" aria-label="State map button"></div>
    </div>
    <div class="navbar__title">Title</div>
    <div class="navbar__actions">
      <svg width="20" height="20" viewBox="0 0 20 20"><circle cx="10" cy="10" r="10" fill="#1e8ad6"/><text x="10" y="14.5" text-anchor="middle" font-family="Roboto, sans-serif" font-size="13" font-weight="500" fill="#000">?</text></svg>
      <svg width="20" height="20" viewBox="0 0 20 20"><g fill="#1e8ad6"><circle cx="10" cy="10" r="6.5"/><g stroke="#1e8ad6" stroke-width="3.4"><path d="M10 1v18M1 10h18M3.6 3.6l12.8 12.8M16.4 3.6L3.6 16.4"/></g></g><circle cx="10" cy="10" r="3" fill="#000"/></svg>
    </div>
  </div>
  <div class="bill-title">Crimes Amendment (Safe Roads) Bill 2015
    <svg width="22" height="22" viewBox="0 0 22 22"><rect x="7" y="5" width="8" height="11" fill="none" stroke="#444" stroke-width="1"/><path d="M8.5 8h5M8.5 10h5M8.5 12h5" stroke="#444" stroke-width=".8"/><circle cx="11" cy="11" r="9.6" fill="none" stroke="#e02a1c" stroke-width="1.6"/><path d="M4.2 4.2l13.6 13.6" stroke="#e02a1c" stroke-width="1.6"/></svg>
  </div>
  <div class="bill-text">Lorem ipsum dolor sit amet, consectetur adipiscing elit. Nam condimentum leo sed nisi malesuada, sed accumsan metus ultricies. Donec eleifend nibh in ultrices tempus. Morbi id tempor lorem. Suspendisse potenti. Fusce at augue pulvinar, ultricies nisl id, bibendum est. Cras semper ac nulla ut vulputate. Nam faucibus sagittis odio, quis molestie elit sollicitudin et. Nam dapibus fringilla orci, quis efficitur leo consectetur eu. Vivamus dui lectus, mollis a condimentum consequat, ullamcorper porta lectus. Vivamus sit amet justo enim. Donec nec lorem mi. Lorem ipsum dolor sit amet, consectetur adipiscing elit. Nam condimentum leo sed nisi malesuada, sed accumsan metus ultricies. Donec eleifend nibh in ultrices tempus. Morbi id tempor lorem. Suspendisse potenti. Fusce at augue pulvinar, ultricies nisl id, bibendum est. Cras semper ac nulla ut vulputate. Nam faucibus sagittis odio, quis molestie elit sollicitudin et. Nam dapibus fringilla orci, quis efficitur leo consectetur eu. Vivamus dui lectus, mollis a condimentum consequat, ullamcorper porta lectus. Vivamus sit amet justo enim. Donec nec lorem mi. Lorem ipsum dolor sit amet, consectetur adipiscing elit. Nam condimentum leo sed nisi malesuada, sed accumsan metus ultricies. Donec eleifend nibh in ultrices tempus. Morbi id tempor lorem. Suspendisse potenti. Fusce at augue pulvinar, ultricies nisl id, bibendum est. Cras semper ac nulla ut vulputate. Nam faucibus sagittis odio, quis molestie elit sollicitudin et. Nam dapibus fringilla orci, quis efficitur leo consectetur eu. Vivamus dui lectus, mollis a condimentum consequat, ullamcorper porta lectus.</div>
  <div class="vote">
    <div class="vote__item vote__item--no">
      <div class="vote__btn"><svg width="14" height="14" viewBox="0 0 14 14"><path d="M2 2l10 10M12 2L2 12" stroke="#fff" stroke-width="1.8"/></svg></div>No
    </div>
    <div class="vote__item vote__item--party">
      <div class="vote__btn"><svg width="16" height="18" viewBox="0 0 16 18"><path d="M1 2h14L8 10z" fill="#fff"/><path d="M8 10v6M4 17h8" stroke="#fff" stroke-width="1.5"/></svg></div>Party
    </div>
    <div class="vote__item vote__item--yes">
      <div class="vote__btn"><svg width="16" height="14" viewBox="0 0 16 14"><path d="M2 7l4.5 4.5L14 3" stroke="#fff" stroke-width="2" fill="none"/></svg></div>Yes
    </div>
  </div>
  <div class="footer"><span class="footer__dot"></span><div class="footer__chamber">Legislative Council</div><div class="footer__count">1 / 77</div></div>
</section>
<div class="screen-caption" style="left:24px">Main Screen</div>

<!-- Options -->
<section class="screen screen--options">
  <div class="status">
    <div class="status__carrier">●●●○○ ORBIT
      <svg width="14" height="11" viewBox="0 0 14 11"><path d="M1 4a9 9 0 0 1 12 0M3.2 6.2a6 6 0 0 1 7.6 0M5.4 8.4a3 3 0 0 1 3.2 0" stroke="#fff" stroke-width="1.5" fill="none"/><circle cx="7" cy="10" r="1" fill="#fff"/></svg>
    </div>
    <div class="status__time">4:21 PM</div>
    <div class="status__battery">
      <svg width="8" height="12" viewBox="0 0 8 12"><path d="M1 3l6 5-3 3V1l3 3-6 5" stroke="#999" stroke-width="1.1" fill="none"/></svg>
      100% <div class="battery"><span></span></div>
    </div>
  </div>
  <div class="navbar">
    <div class="navbar__regions">
      <div class="region region--green" role="img" aria-label="Federal map button"></div>
      <div class="region region--red" role="img" aria-label="State map button"></div>
      <div class="region region--green" role="img" aria-label="Federal map button"></div>
      <div class="region region--red" role="img" aria-label="State map button"></div>
    </div>
    <div class="navbar__title">Title</div>
    <div class="navbar__actions">
      <svg width="20" height="20" viewBox="0 0 20 20"><circle cx="10" cy="10" r="10" fill="#1e8ad6"/><text x="10" y="14.5" text-anchor="middle" font-family="Roboto, sans-serif" font-size="13" font-weight="500" fill="#000">?</text></svg>
      <svg width="20" height="20" viewBox="0 0 20 20"><g fill="#fff"><circle cx="10" cy="10" r="6.5"/><g stroke="#fff" stroke-width="3.4"><path d="M10 1v18M1 10h18M3.6 3.6l12.8 12.8M16.4 3.6L3.6 16.4"/></g></g><circle cx="10" cy="10" r="3" fill="#000"/></svg>
    </div>
  </div>
  <div class="section-head" style="top:72px">Display</div>
  <div class="setting" style="top:128px">Display User Guids <span class="toggle"></span></div>
  <div class="setting" style="top:167px">Hide Bills after Opinion <span class="toggle toggle--on"></span></div>
  <div class="section-head" style="top:217px">Representative Details</div>
  <div class="setting" style="top:272px">Federal Region <span class="setting__value">voxPoll_Federal</span></div>
  <div class="setting" style="top:311px">Federal Representative <span class="setting__value">Aust. Masked Owl</span></div>
  <div class="setting" style="top:350px">State Region <span class="setting__value">voxPoll_NSW</span></div>
  <div class="setting" style="top:389px">State Representative <span class="setting__value">Lesses Sooty Owl</span></div>
  <div class="divider" style="top:429px"></div>
  <div class="legal">
    <div class="legal__version">V0.752</div>
    <div>Federal Bill Details © Federal Bill Registry.</div>
    <div><a href="#">http://www.fedbills.example</a></div>
    <div>NSW Bill Details © State Bill Registry (State Parliament).</div>
    <div><a href="#">http://www.statebills.example</a></div>
  </div>
  <div class="footer"><span class="footer__dot"></span><div class="footer__chamber">House of Representatives</div><div class="footer__count">0 / 0</div></div>
</section>
<div class="screen-caption" style="left:414px">Options Screen</div>

<!-- Help -->
<section class="screen screen--help">
  <div class="status">
    <div class="status__carrier">●●●○○ ORBIT
      <svg width="14" height="11" viewBox="0 0 14 11"><path d="M1 4a9 9 0 0 1 12 0M3.2 6.2a6 6 0 0 1 7.6 0M5.4 8.4a3 3 0 0 1 3.2 0" stroke="#fff" stroke-width="1.5" fill="none"/><circle cx="7" cy="10" r="1" fill="#fff"/></svg>
    </div>
    <div class="status__time">4:21 PM</div>
    <div class="status__battery">
      <svg width="8" height="12" viewBox="0 0 8 12"><path d="M1 3l6 5-3 3V1l3 3-6 5" stroke="#999" stroke-width="1.1" fill="none"/></svg>
      100% <div class="battery"><span></span></div>
    </div>
  </div>
  <div class="navbar">
    <div class="navbar__regions">
      <div class="region region--green" role="img" aria-label="Federal map button"></div>
      <div class="region region--red" role="img" aria-label="State map button"></div>
      <div class="region region--green" role="img" aria-label="Federal map button"></div>
      <div class="region region--red" role="img" aria-label="State map button"></div>
    </div>
    <div class="navbar__title">Title</div>
    <div class="navbar__actions">
      <svg width="20" height="20" viewBox="0 0 20 20"><circle cx="10" cy="10" r="10" fill="#fff"/><text x="10" y="14.5" text-anchor="middle" font-family="Roboto, sans-serif" font-size="13" font-weight="500" fill="#000">?</text></svg>
      <svg width="20" height="20" viewBox="0 0 20 20"><g fill="#1e8ad6"><circle cx="10" cy="10" r="6.5"/><g stroke="#1e8ad6" stroke-width="3.4"><path d="M10 1v18M1 10h18M3.6 3.6l12.8 12.8M16.4 3.6L3.6 16.4"/></g></g><circle cx="10" cy="10" r="3" fill="#000"/></svg>
    </div>
  </div>
  <nav class="tabs">
    <div class="tab tab--active">GENERAL</div>
    <div class="tab">FAQ</div>
    <div class="tab">CONTACT</div>
  </nav>
  <div class="help-text">
    <p>Lorem ipsum dolor sit amet, consectetur adipiscing elit.</p>
    <p>Nam condimentum leo sed nisi malesuada, sed accumsan metus ultricies. Donec eleifend nibh in ultrices tempus. Morbi id tempor lorem. Suspendisse potenti. Fusce at augue pulvinar, ultricies nisl id, bibendum est. Cras semper ac nulla ut vulputate. Nam faucibus sagittis odio, quis molestie elit sollicitudin et. Nam dapibus fringilla orci, quis efficitur leo consectetur eu. Vivamus dui lectus, mollis a condimentum consequat, ullamcorper porta lectus. Vivamus sit amet justo enim. Donec nec lorem mi. Lorem ipsum dolor sit amet, consectetur adipiscing elit.</p>
    <p>Nam condimentum leo sed nisi malesuada, sed accumsan metus ultricies. Donec eleifend nibh in ultrices tempus. Morbi id tempor lorem. Suspendisse potenti. Fusce at augue pulvinar, ultricies nisl id, bibendum est. Cras semper ac nulla ut vulputate. Nam faucibus sagittis odio, quis molestie elit sollicitudin et. Nam dapibus fringilla orci, quis efficitur leo consectetur eu. Vivamus dui lectus, mollis a condimentum consequat, ullamcorper porta lectus. Vivamus sit amet justo enim. Donec nec lorem mi. Lorem ipsum dolor sit amet, consectetur adipiscing elit.</p>
    <p>Nam condimentum leo sed nisi malesuada, sed accumsan metus ultricies. Donec eleifend nibh in ultrices tempus. Morbi id tempor lorem. Suspendisse potenti. Fusce at augue pulvinar, ultricies nisl id, bibendum est. Cras semper ac nulla ut vulputate. Nam faucibus sagittis odio, quis molestie elit sollicitudin et. Nam dapibus fringilla orci, quis efficitur leo consectetur eu. Vivamus dui lectus, mollis a condimentum consequat, ullamcorper porta lectus.</p>
  </div>
  <div class="footer"><span class="footer__dot"></span><div class="footer__chamber">Legislative Council</div><div class="footer__count">1 / 77</div></div>
</section>
<div class="screen-caption" style="left:804px">Help Screen</div>

</body>
</html>
```